New homepage design www.quillharbor.nl

We need a new website design to go with our new designed logo.
We are a relativly small basketballclub that would like a shiny new webdesign for our homepage. We want te be able to create a real homepage/base for our clubmembers, where they can find news, upcoming events (agenda/calendar) and the related info on playing basketball at our club (games/tasks/teams and all).

The current website is located at: www.quillharbor.nl but is an outdated and not so appealing design.
There are no real designfeatures of the current site that have to be transferred to the new site.
Coding in HTML/CSS/JS/JPEG/PNG is enough, making a dynamic website will be my task. I just need the design in HTML (preferrably HTML 5)

There is not a huge budget, we are a club without a main sponsor.

Feel free to be creative and amaze us!

Text for the page in the new design will be created by us, you may use some sample text for filling.

Currently used pictures in the site don't have to be transferred to the new page (preferrably not!)
Updates

Tomorrow we will pick a design.

Industry/Entity Type

Events

Requirements
Must have
• The new logo as uploaded and attached.
News page.
Agenda page
HTML compatible same look and feel in all modern browsers (IE, FireFox, Chrome, Safari)
Nice to have
• HTML 5 validated and approved

```html
<!DOCTYPE html>
<html lang="nl">
<head>
<meta charset="utf-8">
<title>Quillharbor – Basketbalclub</title>
<link rel="stylesheet" href="https://fonts.googleapis.com/css2?family=Anton&family=Oswald:wght@400;500&family=Arimo:ital,wght@0,400;1,400&display=swap">
<style>
:root{
  --orange:#ec8a33;
  --orange-dark:#d9741d;
  --navy-deep:#0f1e2f;
  --navy:#1f3650;
  --navy-mid:#1a2d44;
  --navy-foot:#15263a;
  --white:#ffffff;
  --ink:#121212;
  --muted:#c9d2dc;
}
*{margin:0;padding:0;box-sizing:border-box}
html,body{width:978px;height:1200px;overflow:hidden;background:var(--navy-foot)}
body{position:relative;font-family:"Arimo",Arial,sans-serif;color:var(--white)}
.abs{position:absolute}
.heading{font-family:"Oswald",sans-serif;font-weight:400;text-transform:uppercase;letter-spacing:-.2px}

/* hero */
.hero{left:0;top:0;width:978px;height:464px;
  background:radial-gradient(ellipse at 45% 55%,#b88555 0%,#8a5a36 35%,#3a2a24 70%,#1c1a22 100%)}
.brand{left:150px;top:40px;display:flex;align-items:center;gap:8px;
  font-family:"Oswald",sans-serif;font-weight:500;font-size:26px;color:var(--white);letter-spacing:.5px}
.brand-dot{width:22px;height:22px;border-radius:50%;background:var(--orange)}
.main-nav{top:25px;left:0;width:978px;height:14px}
.main-nav a{position:absolute;font-family:"Oswald",sans-serif;font-size:9.5px;color:var(--white);text-decoration:none;text-transform:uppercase}
.hero-title{left:568px;top:184px;font-family:"Anton",sans-serif;font-weight:400;font-size:42px;line-height:45px;text-transform:uppercase;color:var(--ink)}
.hero-title .light{color:var(--white)}
.slide-arrow{top:248px;width:36px;height:36px;border-radius:50%;border:2px solid rgba(255,255,255,.35);background:rgba(0,0,0,.15)}

/* info band */
.info-band{left:0;top:464px;width:978px;height:69px;background:var(--navy-deep)}
.info-title{left:148px;top:13px;font-size:14.5px;color:var(--orange)}
.info-text{left:148px;top:39px;width:503px;font-size:10px;color:var(--white);white-space:nowrap;overflow:hidden;text-overflow:ellipsis}
.connect-btn{left:661px;top:17px;width:168px;height:35px;border-radius:2px;
  background:linear-gradient(#d6d6d6,#9a9a9a);box-shadow:0 1px 2px rgba(0,0,0,.5);
  font-family:"Oswald",sans-serif;font-size:12.5px;color:#4c4c4c;display:flex;align-items:center;justify-content:center;letter-spacing:.5px}

/* welcome */
.welcome{left:0;top:533px;width:978px;height:173px;background:var(--navy)}
.welcome-title{left:149px;top:27px;font-size:22px;color:var(--orange)}
.welcome-sub{left:149px;top:59px;font-size:18px;color:var(--white)}
.welcome-text{left:149px;top:95px;width:600px;font-size:9.3px;line-height:18.4px;color:var(--white)}

/* events */
.events{left:0;top:706px;width:978px;height:294px;background:var(--navy-mid)}
.section-title{font-size:20px;color:var(--orange)}
.events .section-title{left:147px;top:17px}
.pager{display:flex;gap:2px}
.pager span{width:17px;height:17px;background:var(--orange);display:flex;align-items:center;justify-content:center}
.events .pager{left:794px;top:20px}
.event-card{top:56px;width:211px;height:200px}
.event-photo{width:211px;height:122px}
.date-box{left:0;top:122px;width:32px}
.date-month{height:29px;background:var(--orange);font-family:"Oswald",sans-serif;font-size:10px;display:flex;align-items:center;justify-content:center}
.date-day{margin-top:1px;height:29px;background:var(--orange);text-align:center;font-family:"Oswald",sans-serif;font-size:11px;line-height:12px;padding-top:3px}
.date-day small{display:block;font-size:6.5px;line-height:8px}
.event-title{left:43px;top:132px;font-size:10px;color:var(--orange);white-space:nowrap}
.event-text{left:44px;top:150px;width:160px;font-size:7.6px;line-height:14px;color:var(--white)}

/* news */
.news{left:0;top:1000px;width:978px;height:122px;background:var(--navy)}
.news .section-title{left:159px;top:27px}
.news .pager{left:228px;top:57px}
.news-item{left:280px;top:24px;width:552px;height:78px;background:var(--navy-mid)}
.news-title{left:19px;top:16px;font-size:10px;color:var(--orange)}
.news-date{right:19px;top:18px;font-size:7.5px;font-style:italic;color:var(--orange)}
.news-text{left:20px;top:36px;width:515px;font-size:7.6px;line-height:14px;font-style:italic;color:var(--white)}

/* footer */
.site-footer{left:0;top:1122px;width:978px;height:78px;background:var(--navy-foot)}
.foot-nav{left:150px;top:25px;display:flex;align-items:center;font-family:"Oswald",sans-serif;font-size:7.3px;text-transform:uppercase}
.foot-nav a{color:var(--white);text-decoration:none}
.foot-nav i{display:inline-block;width:1px;height:8px;background:var(--white);margin:0 13px}
.copyright{left:150px;top:51px;font-family:"Oswald",sans-serif;font-size:7px;color:var(--white)}
.social{left:702px;top:35px;display:flex;gap:18px}
.social span{width:11px;height:11px;border-radius:50%;background:var(--muted)}
</style>
</head>
<body>

<header class="hero abs" role="img" aria-label="Basketbalfoto: spelers onder de basket tijdens een wedstrijd op een houten vloer">
  <div class="brand abs"><span class="brand-dot"></span>QUILLHARBOR</div>
  <nav class="main-nav abs">
    <a style="left:297px">Quillharbor</a>
    <a style="left:378px">Teams</a>
    <a style="left:434px">Informatie</a>
    <a style="left:510px">Fotogalerij</a>
    <a style="left:591px">Contact</a>
    <a style="left:656px">Links</a>
    <a style="left:709px">Gastenboek</a>
    <a style="left:789px">Inloggen</a>
  </nav>
  <div class="slide-arrow abs" style="left:86px"></div>
  <div class="slide-arrow abs" style="left:854px"></div>
  <h1 class="hero-title abs"><span class="light">Welkom in het</span><br>gastenboek van<br>Quillharbor!</h1>
</header>

<section class="info-band abs">
  <h2 class="info-title heading abs">Quill Harbor team information</h2>
  <p class="info-text abs">EDANKT! Iedereen ontzettend bedankt voor de leuke feestavond!!!!!! De gezellige bekende sfeer binnen ons...</p>
  <div class="connect-btn abs">CONNECT WITH US</div>
</section>

<section class="welcome abs">
  <h2 class="welcome-title heading abs">Welcome to Quill Harbor</h2>
  <h3 class="welcome-sub heading abs">Het bestuur van BC Quillharbor heet je welkom op onze site.</h3>
  <p class="welcome-text abs">BEDANKT! Iedereen ontzettend bedankt voor de leuke feestavond!!!!!! De gezellige bekende sfeer binnen Quillharbor is de hele avond aanwezig geweest. Super!!!! Iedereen bedankt voor jullie komst, leuke herinneringen en gezelligheid!! Een speciaal bedankje voor de organisatie van het grote Quillharbor spel. Dit was geweldig!!! Bedankt!</p>
</section>

<section class="events abs">
  <h2 class="section-title heading abs">Upcoming events</h2>
  <div class="pager abs">
    <span><svg width="5" height="7" viewBox="0 0 5 7"><path d="M4 .5 1 3.5 4 6.5" fill="none" stroke="#fff"/></svg></span>
    <span><svg width="5" height="7" viewBox="0 0 5 7"><path d="M1 .5 4 3.5 1 6.5" fill="none" stroke="#fff"/></svg></span>
  </div>

  <article class="event-card abs" style="left:147px">
    <div class="event-photo" role="img" aria-label="Foto van handen die een basketbal bij de basket grijpen" style="background:linear-gradient(135deg,#2a2a2a,#7a5a44 55%,#1a1a1a)"></div>
    <div class="date-box abs"><div class="date-month">JAN</div><div class="date-day">15<small>2014</small></div></div>
    <h3 class="event-title heading abs">Geen training ivm Sinterklaas</h3>
    <p class="event-text abs">Edereen ontzettend bedankt voor de leuke feestavond!!!!!! De gezellige bekende sfeer binnen Quillharbor is de hele avond aanwezig geweest. Super!!!! Iedereen...</p>
  </article>

  <article class="event-card abs" style="left:384px">
    <div class="event-photo" role="img" aria-label="Foto van een feestavond met mensen aan tafels onder lichtjes" style="background:linear-gradient(160deg,#1d1a22,#5a3a2c 60%,#2a1c1c)"></div>
    <div class="date-box abs"><div class="date-month">JAN</div><div class="date-day">15<small>2014</small></div></div>
    <h3 class="event-title heading abs">Geen training ivm Sinterklaas</h3>
    <p class="event-text abs">Edereen ontzettend bedankt voor de leuke feestavond!!!!!! De gezellige bekende sfeer binnen Quillharbor is de hele avond aanwezig geweest. Super!!!! Iedereen...</p>
  </article>

  <article class="event-card abs" style="left:621px">
    <div class="event-photo" role="img" aria-label="Foto van een basketballer die springt in een verlichte zaal" style="background:radial-gradient(ellipse at 50% 30%,#3e4a66,#15192a 75%)"></div>
    <div class="date-box abs"><div class="date-month">JAN</div><div class="date-day">15<small>2014</small></div></div>
    <h3 class="event-title heading abs">Geen training ivm Sinterklaas</h3>
    <p class="event-text abs">Edereen ontzettend bedankt voor de leuke feestavond!!!!!! De gezellige bekende sfeer binnen Quillharbor is de hele avond aanwezig geweest. Super!!!! Iedereen...</p>
  </article>
</section>

<section class="news abs">
  <h2 class="section-title heading abs">Latest news</h2>
  <div class="pager abs">
    <span><svg width="5" height="7" viewBox="0 0 5 7"><path d="M4 .5 1 3.5 4 6.5" fill="none" stroke="#fff"/></svg></span>
    <span><svg width="5" height="7" viewBox="0 0 5 7"><path d="M1 .5 4 3.5 1 6.5" fill="none" stroke="#fff"/></svg></span>
  </div>
  <article class="news-item abs">
    <h3 class="news-title heading abs">Geen training ivm Sinterklaas</h3>
    <p class="news-date abs">Posted on 15 DSec 2013</p>
    <p class="news-text abs">Edereen ontzettend bedankt voor de leuke feestavond!!!!!! De gezellige bekende sfeer binnen Quillharbor is de hele avond aanwezig geweest. Super!!!! Iedereen...</p>
  </article>
</section>

<footer class="site-footer abs">
  <nav class="foot-nav abs">
    <a>Quillharbor</a><i></i><a>Teams</a><i></i><a>Informatie</a><i></i><a>Fotogalerij</a><i></i><a>Contact</a><i></i><a>Links</a><i></i><a>Gastenboek</a><i></i><a>Inloggen</a>
  </nav>
  <p class="copyright abs">© 2013 QUILL HARBOR ALL RIGHTS RESERVED</p>
  <div class="social abs" aria-label="Sociale media"><span></span><span></span><span></span><span></span><span></span></div>
</footer>

</body>
</html>
```